8" x 11" One Page Flyer for Fence Installation Company

We are looking to promote our business with a new flyer that would be handed out in person to people or put at their mailbox/door at their homes. The flyer needs to be creative and attention-grabbing. I have attached some of our previous flyers and our website information. Do not call or email regarding the flyer. We want the flyer to look professional but also friendly. One page, NOT folded. You can use images from our website at www.MyBraxtonYard.com or our Facebook page at www.Facebook.com/HollowbrookRailsBKT. We are flexible with what photos you can use but there must be photos of OUR fences on the flyer. More photos specifically can also be provided. Colors need to be suitable for a flyer printed on canary yellow in color paper OR white paper.

Target Market(s)

Homeowners that need a new fence

Industry/Entity Type

Construction

Font styles to use
Sans Serif
Other font styles liked:
• HD Colton

Colors
0054AA
0677BA
7BADD7
CADEEF
E8F1F8
0094D4
00A9DD
6FCCEA
C7EBF8
E9F6FB

Requirements
Must have
• Our fence photos - mostly wood fence photos (different designs), SIZE SHOULD BE LETTER SIZE 8" x 11"
Nice to have
• A nice bible verse featured at the bottom of the flyer.
Should not have
• DO NOT COPY THE WEBSITE FORMAT, I WANT SOMETHING UNIQUE. Other people's fence photos, they must all come from our website or facebook page

```html
<!DOCTYPE html>
<html lang="en">
<head>
<meta charset="utf-8">
<title>Hollowbrook Rails – Fence Flyer</title>
<link rel="stylesheet" href="https://fonts.googleapis.com/css2?family=Oswald:wght@600;700&family=Exo+2:wght@400;500;600;700&display=swap">
<style>
  :root{
    --page:#e6e6e6;
    --paper:#ffffff;
    --brown:#5a3b27;
    --blue:#2f86d1;
    --ink:#1d1d1d;
    --white:#ffffff;
    --map-border:#3f86d6;
  }
  *{box-sizing:border-box;margin:0;padding:0}
  html,body{width:1200px;height:1090px;overflow:hidden;background:var(--page)}
  .flyer{position:absolute;left:200px;top:28px;width:800px;height:1035px;background:var(--paper);overflow:hidden;font-family:"Exo 2",sans-serif;color:var(--brown)}
  .flyer-shapes{position:absolute;inset:0}
  .headline-box{position:absolute;left:30px;top:60px;width:370px;height:270px;background:var(--brown);color:var(--white);padding:28px 30px 0}
  .headline{font-family:"Oswald",sans-serif;font-weight:700;font-size:86px;line-height:.92;letter-spacing:1px;text-transform:uppercase}
  .headline-rule{height:2px;background:var(--white);margin:14px 0 8px}
  .subhead{font-weight:700;font-size:25px;line-height:1.05}
  .brand{position:absolute;left:420px;top:62px;display:flex;align-items:center;gap:14px}
  .brand-mark{width:58px;height:58px;background:var(--brown)}
  .brand-name{font-weight:700;font-size:26px;color:var(--blue);line-height:1}
  .brand-phone{font-weight:700;font-size:27px;color:var(--ink);line-height:1.1}
  .brand-tagline{font-size:9.5px;font-weight:600;color:var(--ink)}
  .why{position:absolute;left:48px;top:355px;width:380px}
  .why-title{font-weight:700;font-size:30px;letter-spacing:.5px}
  .why-lede{font-size:18px;line-height:1.15;margin:6px 0 10px}
  .benefits{list-style:none}
  .benefits li{display:flex;align-items:center;gap:8px;font-weight:600;font-size:17.5px;line-height:1.28}
  .tick{width:14px;height:14px;flex:none}
  .showroom{position:absolute;left:48px;top:690px;width:360px;color:var(--white);font-weight:600;font-size:17px;line-height:1.2}
  .map{position:absolute;left:72px;top:812px;width:330px;height:130px;background:linear-gradient(135deg,#e9eef0,#d9e6df);border:4px solid var(--map-border)}
  .contacts{position:absolute;left:72px;top:958px;list-style:none;color:var(--white);font-weight:600;font-size:20px;line-height:1.28}
  .contacts li{display:flex;align-items:center;gap:10px}
  .contact-icon{width:18px;height:18px;flex:none}
</style>
</head>
<body>
<main class="flyer">
  <svg class="flyer-shapes" width="800" height="1035" viewBox="0 0 800 1035">
    <defs>
      <linearGradient id="fence-photo" x1="0" y1="0" x2="1" y2="1">
        <stop offset="0" stop-color="#6f8a4a"/>
        <stop offset=".45" stop-color="#c9a572"/>
        <stop offset="1" stop-color="#e3bf83"/>
      </linearGradient>
    </defs>
    <rect class="bottom-band" x="0" y="660" width="800" height="375" fill="var(--brown)"/>
    <circle class="photo-ring" cx="790" cy="600" r="400" fill="var(--brown)"/>
    <circle class="fence-photos" cx="790" cy="600" r="380" fill="url(#fence-photo)" role="img" aria-label="Collage of installed wood picket and metal fences and gates"/>
  </svg>

  <section class="headline-box">
    <h1 class="headline">We Build<br>Fences</h1>
    <div class="headline-rule"></div>
    <p class="subhead">And we would love to build<br>your fence too!</p>
  </section>

  <header class="brand">
    <div class="brand-mark"></div>
    <div>
      <div class="brand-name">Hollowbrook Rails</div>
      <div class="brand-phone">555-310-4782</div>
      <div class="brand-tagline">"Because Good Fences Make Good Neighbors"</div>
    </div>
  </header>

  <section class="why">
    <h2 class="why-title">WHY CHOOSE US?</h2>
    <p class="why-lede">Beautiful, professionally installed<br>fences at affordable prices!</p>
    <ul class="benefits">
      <li><svg class="tick" viewBox="0 0 14 14"><circle cx="7" cy="7" r="6" fill="none" stroke="currentColor" stroke-width="1.4"/><path d="M4 7.2l2 2 4-4.2" fill="none" stroke="currentColor" stroke-width="1.6"/></svg>Free Estimates</li>
      <li><svg class="tick" viewBox="0 0 14 14"><circle cx="7" cy="7" r="6" fill="none" stroke="currentColor" stroke-width="1.4"/><path d="M4 7.2l2 2 4-4.2" fill="none" stroke="currentColor" stroke-width="1.6"/></svg>Professional Installation</li>
      <li><svg class="tick" viewBox="0 0 14 14"><circle cx="7" cy="7" r="6" fill="none" stroke="currentColor" stroke-width="1.4"/><path d="M4 7.2l2 2 4-4.2" fill="none" stroke="currentColor" stroke-width="1.6"/></svg>Concrete in EVERY Post</li>
      <li><svg class="tick" viewBox="0 0 14 14"><circle cx="7" cy="7" r="6" fill="none" stroke="currentColor" stroke-width="1.4"/><path d="M4 7.2l2 2 4-4.2" fill="none" stroke="currentColor" stroke-width="1.6"/></svg>HOA Submission Assistance</li>
      <li><svg class="tick" viewBox="0 0 14 14"><circle cx="7" cy="7" r="6" fill="none" stroke="currentColor" stroke-width="1.4"/><path d="M4 7.2l2 2 4-4.2" fill="none" stroke="currentColor" stroke-width="1.6"/></svg>Lifetime Workmanship Warranty</li>
      <li><svg class="tick" viewBox="0 0 14 14"><circle cx="7" cy="7" r="6" fill="none" stroke="currentColor" stroke-width="1.4"/><path d="M4 7.2l2 2 4-4.2" fill="none" stroke="currentColor" stroke-width="1.6"/></svg>Experienced Installation Teams</li>
      <li><svg class="tick" viewBox="0 0 14 14"><circle cx="7" cy="7" r="6" fill="none" stroke="currentColor" stroke-width="1.4"/><path d="M4 7.2l2 2 4-4.2" fill="none" stroke="currentColor" stroke-width="1.6"/></svg>Quality Workmanship &amp; Materials</li>
      <li><svg class="tick" viewBox="0 0 14 14"><circle cx="7" cy="7" r="6" fill="none" stroke="currentColor" stroke-width="1.4"/><path d="M4 7.2l2 2 4-4.2" fill="none" stroke="currentColor" stroke-width="1.6"/></svg>FREE Gate Adjustments for LIFE</li>
    </ul>
  </section>

  <section class="showroom">
    <p>Visit our indoor &amp; outdoor showroom!<br>Our outdoor showroom is open 24/7<br>while our indoor showroom and office is open<br>Monday - Thurs 9AM - 3PM<br>Friday 9AM - 1PM</p>
  </section>

  <div class="map" role="img" aria-label="Street map showing the showroom location"></div>

  <ul class="contacts">
    <li><svg class="contact-icon" viewBox="0 0 18 18"><path d="M4 2l3 3-1.5 2a9 9 0 0 0 5.5 5.5L13 11l3 3-2 2C8 16 2 10 2 4z" fill="none" stroke="currentColor" stroke-width="1.5"/></svg>555-310-4782</li>
    <li><svg class="contact-icon" viewBox="0 0 18 18"><rect x="2" y="4" width="14" height="10" fill="none" stroke="currentColor" stroke-width="1.5"/><path d="M2 4l7 6 7-6" fill="none" stroke="currentColor" stroke-width="1.5"/></svg>office@mybraxtonyard.com</li>
    <li><svg class="contact-icon" viewBox="0 0 18 18"><circle cx="9" cy="9" r="7" fill="none" stroke="currentColor" stroke-width="1.5"/><ellipse cx="9" cy="9" rx="3" ry="7" fill="none" stroke="currentColor" stroke-width="1.2"/><path d="M2 9h14" stroke="currentColor" stroke-width="1.2"/></svg>www.MyBraxtonYard.com</li>
  </ul>
</main>
</body>
</html>
```